Anesthesia Medical Practice Business Card

We need a business card to hand out to surgeons with my basic information. Something that stands out but is not over the top. The medical community is rather conservative. I'd like them to call me first when flipping through their rolodex of anesthesiologists. I'd like the card to communicate confidence, control, professionalism yet serenity. I don't want the card to be pricey to print.

he logo will be provided as a vector graphic in addition to a complete business card design including the logo

Ravi Pell Okonedo, M.D.
Board Certified Anesthesiologist

(310) 555-0186

rokonedo@mailvane.net

Mailing Address:
48315 Corbel Ave.
Suite 270-4863
Los Angeles, CA 90024

A logo that inegrates my initials perhaps
RO MD
My initials are RO and MD as in Medical Doctor

or
perhaps a physician in surgical mask and cap caring for a patient

Target Market(s)

Surgeons who need anesthesia services

Industry/Entity Type

Medical

Requirements
Must have
• the logo will be provided as a vector graphic in addition to a complete business card design including the logo

Ravi Pell Okonedo, M.D.

(310) 555-0186

rokonedo@mailvane.net

Mailing Address:
48315 Corbel Ave.
Suite 270-4863
Los Angeles, CA 90024

Nice to have
• A logo that inegrates my initials perhaps
RO MD

or

```html
<!DOCTYPE html>
<html lang="en">
<head>
<meta charset="utf-8">
<title>Ravi Pell Okonedo, M.D. — Business Card</title>
<link rel="stylesheet" href="https://fonts.googleapis.com/css2?family=Questrial&display=swap">
<style>
  :root {
    --backdrop: #e7e4df;
    --card: #2f3a3c;
    --accent: #e0512a;
    --ink: #ffffff;
    --card-shadow: rgba(0, 0, 0, 0.18);
  }
  * { box-sizing: border-box; margin: 0; padding: 0; }
  html, body {
    width: 1200px;
    height: 1000px;
    overflow: hidden;
    background: var(--backdrop);
    font-family: "Questrial", "Century Gothic", sans-serif;
  }
  .sheet {
    position: relative;
    width: 1200px;
    height: 1000px;
  }
  .card {
    position: absolute;
    left: 220px;
    width: 760px;
    height: 434px;
    background: var(--card);
    border-radius: 30px;
    box-shadow: 0 6px 18px var(--card-shadow);
    color: var(--ink);
    overflow: hidden;
  }
  .card--front { top: 44px; }
  .card--back { top: 522px; }

  /* Front */
  .front-mark {
    position: absolute;
    left: 0;
    right: 0;
    top: 118px;
    text-align: center;
  }
  .wordmark {
    font-size: 112px;
    line-height: 1;
    letter-spacing: 10px;
    color: var(--ink);
  }
  .front-specialty {
    margin-top: 14px;
    font-size: 44px;
    letter-spacing: 1px;
    color: var(--ink);
  }

  /* Back */
  .identity {
    position: absolute;
    left: 84px;
    top: 56px;
  }
  .identity__name {
    font-size: 34px;
    font-weight: 400;
    color: var(--accent);
    letter-spacing: 0.5px;
  }
  .identity__title {
    margin-top: 4px;
    font-size: 24px;
    color: var(--ink);
  }
  .back-mark {
    position: absolute;
    right: 110px;
    top: 122px;
    font-size: 48px;
    letter-spacing: 5px;
    color: var(--ink);
  }
  .address {
    position: absolute;
    left: 84px;
    top: 234px;
    font-size: 24px;
    line-height: 1.3;
    font-style: normal;
  }
  .address__label { color: var(--accent); }
  .contact {
    position: absolute;
    left: 420px;
    right: 40px;
    top: 300px;
    list-style: none;
    font-size: 24px;
  }
  .contact__item {
    display: flex;
    align-items: center;
    gap: 14px;
    margin-bottom: 26px;
    white-space: nowrap;
  }
  .contact__icon { width: 20px; height: 22px; flex: none; }
</style>
</head>
<body>
<main class="sheet">
  <section class="card card--front" aria-label="Card front">
    <div class="front-mark">
      <div class="wordmark">RO MD</div>
      <div class="front-specialty">Anesthesiologist</div>
    </div>
  </section>

  <section class="card card--back" aria-label="Card back">
    <header class="identity">
      <h1 class="identity__name">Ravi Pell Okonedo, M.D.</h1>
      <p class="identity__title">Board Certified Anesthesiologist</p>
    </header>

    <div class="back-mark">RO MD</div>

    <address class="address">
      <div class="address__label">Mailing Address:</div>
      <div>48315 Corbel Ave.</div>
      <div>Suite 270-4863</div>
      <div>Los Angeles, CA 90024</div>
    </address>

    <ul class="contact">
      <li class="contact__item">
        <svg class="contact__icon" viewBox="0 0 20 22" aria-hidden="true">
          <rect x="4" y="1" width="12" height="20" rx="2" fill="none" stroke="#e0512a" stroke-width="2"/>
          <line x1="8" y1="17" x2="12" y2="17" stroke="#e0512a" stroke-width="2"/>
        </svg>
        <span>(310) 555-0186</span>
      </li>
      <li class="contact__item">
        <svg class="contact__icon" viewBox="0 0 20 22" aria-hidden="true">
          <rect x="1" y="5" width="18" height="12" fill="none" stroke="#e0512a" stroke-width="2"/>
          <polyline points="1,5 10,12 19,5" fill="none" stroke="#e0512a" stroke-width="2"/>
        </svg>
        <span>rokonedo@mailvane.net</span>
      </li>
    </ul>
  </section>
</main>
</body>
</html>
```